R&T Builders and Spaces Business Card

We need to redesign our business card. We had used white vellum wih grey logo and txt in the past. I would like to bring a little life into our cards without being over the top. I think I will be going away from the vellum and printing soft touch business cards.
I have attached what we currently have and our new logo design.

```html
<!DOCTYPE html>
<html lang="en">
<head>
<meta charset="utf-8">
<title>R&amp;T Builders and Spaces – Business Card</title>
<link href="https://fonts.googleapis.com/css2?family=Jost:wght@400;500;600&amp;family=Montserrat:wght@400;500&amp;display=swap" rel="stylesheet">
<style>
  :root {
    --backdrop: #c9c9c9;
    --card: #ffffff;
    --ink: #3a3a3a;
    --ink-soft: #444444;
  }
  * { margin: 0; padding: 0; box-sizing: border-box; }
  html, body {
    width: 1200px;
    height: 896px;
    overflow: hidden;
    background: var(--backdrop);
  }
  .canvas {
    position: relative;
    width: 1200px;
    height: 896px;
  }
  .card {
    position: absolute;
    left: 334px;
    width: 528px;
    height: 301px;
    background: var(--card);
    border-radius: 24px;
  }
  .card--front { top: 125px; }
  .card--back  { top: 474px; }

  /* wordmark block standing where the mark sits */
  .wordmark {
    position: absolute;
    display: flex;
    flex-direction: column;
    align-items: center;
    justify-content: center;
    gap: 14px;
    text-align: center;
  }
  .wordmark__square {
    width: 34px;
    height: 34px;
    background: var(--ink);
  }
  .wordmark__name {
    font-family: "Jost", sans-serif;
    font-weight: 500;
    color: var(--ink);
    letter-spacing: 0.12em;
    text-transform: uppercase;
    line-height: 1.35;
  }
  .card--front .wordmark {
    left: 38px; top: 63px; width: 177px; height: 177px;
  }
  .card--front .wordmark__name { font-size: 15px; }
  .card--back .wordmark {
    left: 166px; top: 54px; width: 196px; height: 195px;
  }
  .card--back .wordmark__name { font-size: 17px; }

  .divider {
    position: absolute;
    left: 233px;
    top: 67px;
    width: 1.5px;
    height: 169px;
    background: var(--ink);
  }
  .details {
    position: absolute;
    left: 255px;
    top: 64px;
    color: var(--ink-soft);
  }
  .details__name {
    font-family: "Jost", sans-serif;
    font-weight: 600;
    font-size: 20px;
    letter-spacing: 0.02em;
    line-height: 1;
    color: var(--ink);
  }
  .details__title {
    font-family: "Jost", sans-serif;
    font-weight: 400;
    font-size: 18px;
    letter-spacing: 0.03em;
    line-height: 1;
    margin-top: 2px;
  }
  .contact-list {
    list-style: none;
    margin-top: 12px;
    font-family: "Montserrat", sans-serif;
    font-size: 13px;
    line-height: 18.7px;
  }
  .contact-list li {
    display: flex;
    align-items: center;
    gap: 5px;
  }
  .contact-list svg {
    width: 11px;
    height: 11px;
    fill: var(--ink);
    flex: none;
  }
  .address {
    margin-top: 12px;
    font-family: "Montserrat", sans-serif;
    font-size: 13px;
    line-height: 18.5px;
    font-style: normal;
  }
</style>
</head>
<body>
<main class="canvas">

  <section class="card card--front" aria-label="Business card front">
    <div class="wordmark">
      <span class="wordmark__square"></span>
      <span class="wordmark__name">R&amp;T Builders<br>and Spaces</span>
    </div>
    <span class="divider"></span>
    <div class="details">
      <h1 class="details__name">DANA M. HALE</h1>
      <p class="details__title">PRINCIPAL</p>
      <ul class="contact-list">
        <li>
          <svg viewBox="0 0 12 12" aria-hidden="true"><path d="M1 4.5C1 2.8 3 2 6 2s5 .8 5 2.5v1H8.6V4.3H3.4v1.2H1zM3 6h6l1.5 4h-9z"/></svg>
          555 014 2280
        </li>
        <li>
          <svg viewBox="0 0 12 12" aria-hidden="true"><path d="M3.5 0.5h5v11h-5z M4.5 1.5v7.5h3V1.5z" fill-rule="evenodd"/></svg>
          555 017 4409
        </li>
        <li>
          <svg viewBox="0 0 12 12" aria-hidden="true"><path d="M1 3h10v1L6 7 1 4zM1 5.2l5 3 5-3V10H1z"/></svg>
          DANAH@RTBUILDERS.COM
        </li>
        <li>
          <svg viewBox="0 0 12 12" aria-hidden="true"><circle cx="6" cy="6" r="5"/><path d="M6 1v10M1 6h10" stroke="#fff" stroke-width="0.9"/></svg>
          WWW.RTBUILDERS.COM
        </li>
      </ul>
      <address class="address">
        1840 W MESA RIDGE RD, SUITE 210<br>
        FAIRVIEW, OREGON 97024
      </address>
    </div>
  </section>

  <section class="card card--back" aria-label="Business card back">
    <div class="wordmark">
      <span class="wordmark__square"></span>
      <span class="wordmark__name">R&amp;T Builders<br>and Spaces</span>
    </div>
  </section>

</main>
</body>
</html>
```